Flyer Design for mobile emergency tool and vehicle up-fitting services company

trifold flyer design for a uplifting company that does poly - plastic manufacturing for FIRE, EMS and POLICE vehicles. We design and manufacture poly systems for tools, custom storage solutions. We install vehicle lifts, lights, sirens, consoles, cabinets etc. We use CNC to design custom mounting projects for first responders

Target Market(s)

FIRE, EMS, MILITARY and POLICE

Industry/Entity Type

emergency services

Font styles to use
Serif

Colors
EB3D1F
EC4F4E
F09395
F8D3D4
FCEDEE

Requirements
Must have
• multiple pictures
Nice to have
• background design that is related to my current market

```html
<!DOCTYPE html>
<html lang="en">
<head>
<meta charset="utf-8">
<title>Ridgeline Upfitters – Trifold Brochure</title>
<link href="https://fonts.googleapis.com/css2?family=Poppins:wght@400;600;700;800&display=swap" rel="stylesheet">
<style>
:root{
  --stage:#d6d6d6;
  --paper:#ffffff;
  --ink:#3a3a3a;
  --navy:#0d2a78;
  --navy-deep:#0a2466;
  --red:#e0123b;
  --sky:#7ba4dc;
  --black:#000000;
  --band:rgba(40,80,190,.78);
}
*{box-sizing:border-box;margin:0;padding:0}
html,body{width:1006px;height:1200px;overflow:hidden}
body{background:var(--stage);font-family:'Poppins',sans-serif;color:var(--ink);position:relative}
.spread{position:absolute;left:178px;width:663px;height:469px;display:flex}
.spread--outside{top:106px}
.spread--inside{top:631px}
.panel{position:relative;width:221px;height:469px;overflow:hidden}
.panel--white{background:var(--paper)}
.panel--black{background:var(--black);color:#fff;text-align:center}
.panel--navy{background:var(--navy-deep)}
.panel--sky{background:var(--sky)}
.photo{position:absolute}
.section-bar{position:absolute;left:22px;width:180px;height:23px;background:var(--navy);color:#fff;font-weight:700;font-size:14px;line-height:23px;text-align:center}
.body-copy{position:absolute;left:22px;width:180px;font-size:7.6px;line-height:9.5px;text-align:justify}
.body-copy p+p{margin-top:5px}
.brand-mark{display:block;margin:0 auto;border-radius:50%}
.brand-name{font-weight:800;line-height:1.05;text-transform:uppercase}
.quote{position:absolute;left:30px;width:161px;top:218px;font-size:7.8px;line-height:9.6px}
.quote-mark{color:var(--red);font-weight:800;font-size:13px;line-height:0}
.quote-author{margin-top:10px;font-weight:700;font-size:7.6px;letter-spacing:.5px}
.contact-title{position:absolute;top:322px;left:0;width:100%;color:var(--red);font-weight:700;font-size:13px}
.contact-lines{position:absolute;top:350px;left:0;width:100%;font-size:9.4px;line-height:11.4px}
.contact-phone{position:absolute;top:393px;left:0;width:100%;font-weight:700;font-size:12.5px}
.contact-web{position:absolute;top:409px;left:0;width:100%;font-size:9.4px;line-height:11px}
.contact-web strong{font-weight:700;font-size:8.8px}
.big-phone{position:absolute;left:0;width:100%;text-align:center;color:var(--red);font-weight:700;font-size:24px;letter-spacing:.3px}
.url-pill{position:absolute;left:26px;width:168px;height:14px;background:var(--navy);color:#fff;border-radius:8px;font-size:9px;line-height:14px;letter-spacing:2.2px;text-align:center}
.service-title{position:absolute;left:23px;top:13px;width:176px;height:22px;background:var(--red);color:#fff;font-weight:700;font-size:13.5px;line-height:22px;text-align:center}
.service-tile{position:absolute;left:23px;width:175px;height:70px;overflow:hidden}
.service-label{position:absolute;left:0;bottom:0;width:100%;height:16px;background:var(--band);color:#fff;font-weight:700;font-size:9.6px;line-height:16px;text-align:center}
.thumb{position:absolute;width:58px;height:58px;border-radius:50%;border:3px solid #fff}
</style>
</head>
<body>

<!-- Outside spread -->
<section class="spread spread--outside">
  <div class="panel panel--white">
    <div class="photo" role="img" aria-label="Red heavy rescue fire truck with open equipment compartments in a station bay" style="left:22px;top:23px;width:180px;height:77px;background:linear-gradient(180deg,#8b8f96 0%,#b5202a 45%,#8e1419 80%,#5a5a5a 100%)"></div>
    <div class="section-bar" style="top:104px">WHAT WE DO</div>
    <div class="body-copy" style="top:130px">
      <p>Ridgeline Upfitters understands the importance of keeping your first out tools safe, secure, and easily accessible. The task of organizing and securing your equipment while utilizing all of your compartment space can be complicated. Ridgeline makes it easy with a line of products custom built for your needs. It is our duty to produce innovative tool-specific mounting solutions and organizing products to utilize every square inch of the compartment space. All of Ridgeline's components are manufactured from rugged, durable, chemical-resistant, HDPE (high density polyethylene material. This material is non-toxic, has a high degree of stability, and resists degradation.</p>
      <p>Ridgeline is owned and operated by first responders and our company is dedicated to the brothers and sisters that are on the frontline every day.</p>
    </div>
    <div class="photo" role="img" aria-label="Three first responders in uniform holding orange medical bags" style="left:0;top:323px;width:221px;height:146px;background:linear-gradient(180deg,#ffffff 0%,#d9dde3 30%,#2b2f38 70%,#1a1c22 100%)"></div>
  </div>

  <div class="panel panel--black">
    <div style="position:absolute;top:70px;left:0;width:100%">
      <span class="brand-mark" style="width:78px;height:78px;background:#fff"></span>
      <div class="brand-name" style="margin-top:8px;font-size:15px;color:#fff">Ridgeline<br>Upfitters</div>
    </div>
    <div class="quote">
      <span class="quote-mark">&ldquo;</span> Lorem ipsum dolor sit amet, consectetuer adipiscing elit, sed diam nonummy nibh euismod tincidunt ut laoreet dolore magna aliquam erat volutpat. Ut wisi enim ad <span class="quote-mark">&rdquo;</span>
      <div class="quote-author">- DANA REYES</div>
    </div>
    <div class="contact-title">CONTACT US</div>
    <div class="contact-lines">Ridgeline Upfitters<br>412 Harbor View Road<br>Juneau, Alaska 99801</div>
    <div class="contact-phone">555.014.2290</div>
    <div class="contact-web">hello@ridgelineupfit.com<br><strong>RIDGELINEUPFIT.COM</strong></div>
  </div>

  <div class="panel panel--white">
    <div style="position:absolute;top:22px;left:0;width:100%;text-align:center">
      <span class="brand-mark" style="width:78px;height:78px;background:var(--black)"></span>
      <div class="brand-name" style="margin-top:7px;font-size:15px;color:var(--black)">Ridgeline<br>Upfitters</div>
    </div>
    <div class="photo" role="img" aria-label="Pickup truck bed fitted with black storage cabinets and drawers under a blue sky" style="left:0;top:125px;width:221px;height:280px;background:linear-gradient(180deg,#3d7fd6 0%,#7eb0e6 35%,#3a3a3a 60%,#1e1e1e 100%)"></div>
    <svg style="position:absolute;left:0;top:0" width="221" height="469" viewBox="0 0 221 469" aria-hidden="true">
      <path d="M0 0H221V128Q120 175 0 139Z" fill="#fff"/>
      <path d="M0 139Q120 178 221 128" fill="none" stroke="#e0123b" stroke-width="6"/>
      <path d="M0 381Q110 352 221 396" fill="none" stroke="#0d2a78" stroke-width="6"/>
      <path d="M0 384Q110 356 221 399V469H0Z" fill="#fff"/>
    </svg>
    <div class="thumb" role="img" aria-label="Yellow hydraulic rescue tools mounted in a compartment" style="left:20px;top:330px;background:radial-gradient(circle,#e5b220,#5a4a20)"></div>
    <div class="thumb" role="img" aria-label="Red power unit mounted on a bracket" style="left:86px;top:324px;background:radial-gradient(circle,#d9262c,#4a4a4a)"></div>
    <div class="thumb" role="img" aria-label="Black tool mounts in a truck compartment" style="left:152px;top:330px;background:radial-gradient(circle,#9a9a9a,#2a2a2a)"></div>
    <div class="big-phone" style="top:405px">555.014.2290</div>
    <div class="url-pill" style="top:436px">WWW.RIDGELINEUPFIT.COM</div>
  </div>
</section>

<!-- Inside spread -->
<section class="spread spread--inside">
  <div class="panel panel--white">
    <div class="photo" role="img" aria-label="Three firefighters in turnout gear holding helmets in front of a fire engine" style="left:23px;top:24px;width:180px;height:142px;background:linear-gradient(180deg,#b31b24 0%,#8c6b3e 55%,#4a3b28 100%)"></div>
    <div class="section-bar" style="top:175px;left:24px;width:177px">ABOUT US</div>
    <div class="body-copy" style="top:201px;left:24px;width:178px">
      <p>Ridgeline Upfitters understands the importance of keeping your first out tools safe, secure, and easily accessible. The task of organizing and securing your equipment while utilizing all of your compartment space can be complicated. Ridgeline makes it easy with a line of products custom built for your needs. It is our duty to produce innovative tool-specific mounting solutions and organizing products to utilize every square inch of the compartment space. All of Ridgeline's components are manufactured from rugged, durable, chemical-resistant, HDPE (high density polyethylene material. This material is non-toxic, has a high degree of stability, and resists degradation.</p>
      <p style="margin-top:9px">Ridgeline is owned and operated by first responders and our company is dedicated to the brothers and sisters that are on the frontline every day.</p>
      <p style="margin-top:9px">Stop putting your emergency vehicles out of service, we will come to you! We have a mobile fabrication unit that will come onsite for custom installs</p>
    </div>
  </div>

  <div class="panel panel--navy">
    <div class="service-title">OUR SERVICES</div>
    <div class="service-tile" style="top:41px">
      <div class="photo" role="img" aria-label="Red hydraulic rescue tools mounted in a compartment" style="inset:0;background:linear-gradient(135deg,#6a6a6a,#b41a22 50%,#2a2a2a)"></div>
      <div class="service-label">VEHICLE LIFTS</div>
    </div>
    <div class="service-tile" style="top:124px">
      <div class="photo" role="img" aria-label="Yellow tools and scene lights on a compartment wall" style="inset:0;background:linear-gradient(135deg,#c9201f,#e6b12a 45%,#4a4a4a)"></div>
      <div class="service-label">LIGHTS</div>
    </div>
    <div class="service-tile" style="top:208px">
      <div class="photo" role="img" aria-label="Compartment tray with cribbing blocks and power tools" style="inset:0;background:linear-gradient(135deg,#b8894f,#7a7a7a 50%,#2a2a2a)"></div>
      <div class="service-label">SIRENS</div>
    </div>
    <div class="service-tile" style="top:292px">
      <div class="photo" role="img" aria-label="Hose reels and a yellow generator in a truck compartment" style="inset:0;background:linear-gradient(135deg,#9a9ea4,#5a5a5a 50%,#e3c018)"></div>
      <div class="service-label">CONSOLES</div>
    </div>
    <div class="service-tile" style="top:376px">
      <div class="photo" role="img" aria-label="Black storage cabinets installed on a red pickup" style="inset:0;background:linear-gradient(135deg,#1e1e1e,#6c7f6a 50%,#8a1a1e)"></div>
      <div class="service-label">CABINETS</div>
    </div>
  </div>

  <div class="panel panel--sky">
    <div class="photo" role="img" aria-label="Rescue saws and cutters mounted on compartment shelves" style="left:19px;top:19px;width:180px;height:131px;background:linear-gradient(180deg,#b8b8b8 0%,#d56a2a 35%,#3a3a3a 70%,#1c1c1c 100%)"></div>
    <div class="body-copy" style="top:158px;left:20px;width:179px;color:#fff">
      <p>Ridgeline Upfitters understands the importance of keeping your first out tools safe, secure, and easily accessible. The task of organizing and securing your equipment while utilizing all of your compartment space can be complicated. Ridgeline makes it easy with a line of products custom built for your needs. It is our duty to produce innovative tool-specific mounting solutions and organizing products to utilize every square inch of the compartment space. All of Ridgeline's components are manufactured</p>
    </div>
    <div class="big-phone" style="top:280px">555.014.2290</div>
    <div class="url-pill" style="top:311px">WWW.RIDGELINEUPFIT.COM</div>
    <div class="photo" role="img" aria-label="Red fire department pickup with open side compartments holding breathing apparatus" style="left:0;top:323px;width:221px;height:146px;background:linear-gradient(180deg,#7ba4dc 0%,#5a5a5a 35%,#c4161e 70%,#8a1015 100%)"></div>
  </div>
</section>

</body>
</html>
```